依頼詳細
大通りに面していて車で走りながら見てすぐにわかるように、かつ目を引く看板のデザインがいいです。ターゲット層は20才から年配の方までは幅広いですがシンプルで温かみがありわかりやすいデザインを希望します。
記載項目
サイズ:横100cm×縦420cm
建物全体の色が白系統となります。「ギフト専門店」「贈答品専門店」「贈答品」「ギフト」などの何のお店なのか分かる必要があります。また、結婚内祝・出産内祝・景品・香典返しの文言を組み込んで欲しいです。
希望イメージ
シンプル 複雑
単色 カラフル
暗い 明るい
日常 高級
遊び心 厳粛
未来的 伝統的
女性的 男性的
希望する色
特にないですが、店舗全体の色が白系統です。
納品ファイル
• イラストレーター形式 (.ai)
補足説明
イメージデータはハコブネ転送にアップロードしました。
https://73.hakobune-sd.jp/0528-c3d1e8a0f4b72a903e1c5d6084b2f7e6
現在の外観写真を添付します。

シンプルですが、伝えたいことが分かる視認性を重視しました。

この度はコンペ参加ありがとうございます。今後ともよろしくお願いします。

```html
<!DOCTYPE html>
<html lang="ja">
<head>
<meta charset="utf-8">
<title>ギフト 縦看板</title>
<link rel="stylesheet" href="https://fonts.googleapis.com/css2?family=M+PLUS+Rounded+1c:wght@800&display=swap">
<style>
  :root {
    --page: #ffffff;
    --cream: #fdf6d3;
    --rose: #d3195c;
    --rose-deep: #c8185a;
    --rose-light: #f6b6c9;
    --gold: #c99e5e;
    --gold-light: #efd7a6;
    --label: #ffffff;
  }
  * { margin: 0; padding: 0; box-sizing: border-box; }
  html, body { width: 1200px; height: 2705px; overflow: hidden; background: var(--page); }
  .sign {
    position: relative;
    width: 1200px;
    height: 2705px;
    font-family: "M PLUS Rounded 1c", sans-serif;
  }
  .sign-art { position: absolute; inset: 0; }
  .bow {
    position: absolute;
    left: 370px; top: 60px;
    width: 460px; height: 320px;
    border-radius: 45% 45% 30% 30%;
    background: radial-gradient(ellipse at 50% 45%, var(--gold-light), var(--gold));
  }
  .category-title {
    position: absolute;
    left: 0; right: 0; top: 430px;
    text-align: center;
    font-size: 150px;
    line-height: 1;
    color: var(--rose);
    letter-spacing: 6px;
  }
  .occasion-icon {
    position: absolute;
    left: 540px;
    width: 120px; height: 110px;
    border-radius: 50%;
    background: radial-gradient(circle, var(--gold-light), var(--gold));
  }
  .occasion-label {
    position: absolute;
    left: 0; right: 0;
    text-align: center;
    font-size: 96px;
    line-height: 1;
    color: var(--label);
    letter-spacing: 4px;
    text-shadow: 0 4px 8px rgba(120, 0, 40, 0.55);
  }
  .store-name {
    position: absolute;
    left: 0; right: 0; top: 2470px;
    text-align: center;
    font-size: 130px;
    line-height: 1;
    color: var(--rose);
    letter-spacing: 8px;
  }
</style>
</head>
<body>
<main class="sign">
  <svg class="sign-art" width="1200" height="2705" viewBox="0 0 1200 2705" aria-hidden="true">
    <defs>
      <linearGradient id="ribbon-fill" x1="0" y1="0" x2="0" y2="1">
        <stop offset="0" stop-color="#fbd3df"/>
        <stop offset="0.35" stop-color="#e25a88"/>
        <stop offset="1" stop-color="#c8185a"/>
      </linearGradient>
    </defs>
    <rect class="panel" x="200" y="48" width="800" height="2624" fill="var(--cream)"/>
    <rect class="edge-stripe" x="232" y="48" width="12" height="2624" fill="var(--rose)"/>
    <rect class="edge-stripe" x="956" y="48" width="12" height="2624" fill="var(--rose)"/>
    <g class="ribbons" fill="url(#ribbon-fill)">
      <polygon points="244,690 600,790 956,690 956,1030 600,1090 244,1030"/>
      <polygon points="244,1130 600,1230 956,1130 956,1470 600,1530 244,1470"/>
      <polygon points="244,1570 600,1670 956,1570 956,1910 600,1970 244,1910"/>
      <polygon points="244,2010 600,2110 956,2010 956,2350 600,2410 244,2350"/>
    </g>
  </svg>

  <div class="bow" role="img" aria-label="金色のリボン飾り"></div>
  <h1 class="category-title">ギフト</h1>

  <div class="occasion-icon" style="top:675px" role="img" aria-label="指輪のアイコン"></div>
  <p class="occasion-label" style="top:862px">結婚内祝</p>

  <div class="occasion-icon" style="top:1115px" role="img" aria-label="赤ちゃんのアイコン"></div>
  <p class="occasion-label" style="top:1302px">出産内祝</p>

  <div class="occasion-icon" style="top:1555px" role="img" aria-label="トロフィーのアイコン"></div>
  <p class="occasion-label" style="top:1742px">景 品</p>

  <div class="occasion-icon" style="top:1995px" role="img" aria-label="蓮の花のアイコン"></div>
  <p class="occasion-label" style="top:2182px">香典返し</p>

  <p class="store-name">ミレア</p>
</main>
</body>
</html>
```